Rocket business card

Modern business card design, use of color is good with clean space too.

Things to include on card:

Quote: I add fuel to your optometry practice

- Eyewear Sales
- Admin Duties
- Revenue Collection
- Leadership
- Tech Adoption
- COGS Reduction
- Product Sourcing
-Medical Growth

Dalton Vessey, CEO
Glint Harbor
Text Me! 847-302-1964
dalton@glintharbor.example

```html
<!DOCTYPE html>
<html lang="en">
<head>
<meta charset="utf-8">
<title>Glint Harbor – Business Card</title>
<link href="https://fonts.googleapis.com/css2?family=Roboto:ital,wght@0,400;0,500;0,700;1,400&display=swap" rel="stylesheet">
<style>
  :root {
    --backdrop: #e6e1d9;
    --card: #f2f2f2;
    --ink: #111111;
    --band: #050505;
    --band-text: #ffffff;
    --accent: #f0972a;
    --accent-deep: #e5542a;
  }
  * { box-sizing: border-box; margin: 0; padding: 0; }
  html, body {
    width: 900px; height: 1200px; overflow: hidden;
    background: var(--backdrop);
    font-family: "Roboto", Arial, sans-serif;
    color: var(--ink);
  }
  .canvas { position: relative; width: 900px; height: 1200px; }

  .card {
    position: absolute; left: 75px; width: 768px;
    background: var(--card); border-radius: 18px; overflow: hidden;
    box-shadow: 0 6px 16px rgba(0,0,0,0.25);
  }
  .card--front { top: 133px; height: 438px; }
  .card--back { top: 627px; height: 441px; }

  .band {
    position: absolute; left: 0; right: 0; height: 70px;
    background: var(--band); color: var(--band-text);
    display: flex; align-items: center; justify-content: center;
    font-size: 20px; font-weight: 500;
  }
  .band--bottom { bottom: 0; }
  .band--top { top: 0; }

  .tagline { font-style: italic; font-weight: 400; font-size: 21px; }

  .services { display: flex; align-items: center; gap: 12px; white-space: nowrap; }
  .services .sep { font-weight: 400; }
  .services--wide { gap: 24px; }

  .holder { position: absolute; left: 47px; top: 62px; }
  .holder__name {
    color: var(--accent); font-weight: 700; font-size: 41px;
    letter-spacing: 0.5px; line-height: 1;
  }
  .holder__title { font-weight: 500; font-size: 23px; margin-top: 10px; }

  .text-me { position: absolute; left: 36px; top: 195px; }
  .text-me__bubble {
    position: relative; width: 188px; height: 39px;
    background: var(--accent); border-radius: 20px;
    color: #fff; font-weight: 700; font-size: 25px;
    display: flex; align-items: center; justify-content: center; padding-left: 6px;
  }
  .text-me__tail { position: absolute; left: 18px; top: 34px; }

  .contact { position: absolute; left: 43px; top: 274px; }
  .contact__row { display: flex; align-items: center; gap: 8px; font-size: 25px; height: 38px; }
  .contact__icon {
    width: 27px; height: 27px; border-radius: 50%; background: var(--accent);
    display: flex; align-items: center; justify-content: center;
  }

  .brand { position: absolute; display: flex; flex-direction: column; align-items: center; }
  .brand__dot { border-radius: 50%; background: linear-gradient(90deg, var(--accent-deep), var(--accent)); }
  .brand__name { font-weight: 500; color: var(--ink); letter-spacing: 2px; line-height: 1; white-space: nowrap; text-transform: uppercase; }

  .brand--front { left: 385px; top: 52px; width: 336px; }
  .brand--front .brand__dot { width: 100px; height: 100px; }
  .brand--front .brand__name { font-size: 42px; margin-top: 26px; }

  .brand--back { left: 0; right: 0; top: 110px; }
  .brand--back .brand__dot { width: 124px; height: 124px; }
  .brand--back .brand__name { font-size: 56px; margin-top: 42px; }
</style>
</head>
<body>
<main class="canvas">

  <section class="card card--front">
    <div class="holder">
      <p class="holder__name">DALTON VESSEY</p>
      <p class="holder__title">CEO</p>
    </div>

    <div class="text-me">
      <div class="text-me__bubble">Text Me!</div>
      <svg class="text-me__tail" width="22" height="22" viewBox="0 0 22 22"><path d="M0 0 H20 L3 21 Z" fill="var(--accent)"/></svg>
    </div>

    <div class="contact">
      <div class="contact__row">
        <span class="contact__icon">
          <svg width="15" height="15" viewBox="0 0 24 24"><path fill="#fff" d="M6.6 10.8a15.1 15.1 0 0 0 6.6 6.6l2.2-2.2a1 1 0 0 1 1-.25 11.4 11.4 0 0 0 3.6.57 1 1 0 0 1 1 1V20a1 1 0 0 1-1 1A17 17 0 0 1 3 4a1 1 0 0 1 1-1h3.5a1 1 0 0 1 1 1c0 1.25.2 2.45.57 3.57a1 1 0 0 1-.25 1z"/></svg>
        </span>
        <span>847-302-1964</span>
      </div>
      <div class="contact__row">
        <span class="contact__icon">
          <svg width="15" height="15" viewBox="0 0 24 24"><path fill="#fff" d="M3 5h18v14H3z"/><path d="M3 5l9 7 9-7" fill="none" stroke="var(--accent)" stroke-width="2"/></svg>
        </span>
        <span>dalton@glintharbor.example</span>
      </div>
    </div>

    <div class="brand brand--front">
      <span class="brand__dot"></span>
      <span class="brand__name">Glint Harbor</span>
    </div>

    <div class="band band--bottom"><span class="tagline">I add fuel to your optometry practice</span></div>
  </section>

  <section class="card card--back">
    <div class="band band--top">
      <div class="services">
        <span>Tech Adoption</span><span class="sep">|</span>
        <span>COGS Reduction</span><span class="sep">|</span>
        <span>Product Sourcing</span><span class="sep">|</span>
        <span>Medical Growth</span>
      </div>
    </div>

    <div class="brand brand--back">
      <span class="brand__dot"></span>
      <span class="brand__name">Glint Harbor</span>
    </div>

    <div class="band band--bottom">
      <div class="services services--wide">
        <span>Eyewear Sales</span><span class="sep">|</span>
        <span>Admin Duties</span><span class="sep">|</span>
        <span>Revenue Collection</span><span class="sep">|</span>
        <span>Leadership</span>
      </div>
    </div>
  </section>

</main>
</body>
</html>
```